New Website for IT Services Business

We need an uncoded web design for a new company based in Australia called "Falcon IT". We offer specialised point of sale (POS) support to the hospitality industry. We already support hundreds of cafes and restaurants. We are also about to launch and promote a range of new services with the offering of General IT Support being the most important. Other additional services to be offered are Falcon Vault Storage, reselling and supporting Corvel Shieldware and Trelmo Suite.

We have a logo design and our colour scheme is based on the logo with the addition of charcoal grey (see attached logos). We want the pages to reflect precision and efficiency with sharp characteristics. It must be professional but playful/fun elements are encouraged.

Our target audience is restaurant and cafe owners who are interested in finding high quality POS and IT support for their business.

The main call to action on the home page should be either 'Let's Meet For Coffee!' or 'Find out more (by completing a form)'. If you are unsure about what the general text should say then you can use 'Lorem Ipsum' where required.

The site must be viewable at different resolutions and on smart phones and tablets.

The website structure will be quite simple. We require:
- one impressive landing page. Visitors will quickly determine our services and that we provide a very high level of service while also offering value for money. Obviously a clear list of links (however/wherever you like) to the other pages.
- Simple pages with a similar layout for the following:
- Services - "POS & IT Support for the Hospitality Industry" being the main one. With complementary services also listed. Another call to action on this page with the option of 'Let's Meet For Coffee' or a "More information/Pricing" form to be completed by the visitor.
- Products - will be a small online storefront for a few simple products.
- About - Business background. 2x Directors with a photo and brief Bio.
- Downloads - A list of free files to download. Includes remote access client software.
- Contact Us - Mailing address, Email addresses and Support phone number.

Please feel free to ask any questions about the design. I will assist as much as possible.

Thank you for viewing. We promise to give constructive feedback to every person who submits a design. Thank you so much.

Target Market(s)

Restaurant and Cafe owners.

Industry/Entity Type

Hospitality

Requirements
Must have
• - Viewable on different resolutions and on smart phones and tablets.
- Clear call to action of EITHER 'Let's Meet For Coffee' or a "More information/Pricing" form to be completed by the visitor.

```html
<!DOCTYPE html>
<html lang="en">
<head>
<meta charset="utf-8">
<title>Falcon IT</title>
<link rel="stylesheet" href="https://fonts.googleapis.com/css2?family=Oswald:wght@300;400&family=PT+Sans+Narrow&family=Arimo:wght@400;700&display=swap">
<style>
:root{
  --red:#be1e2d;
  --red-dark:#a3172a;
  --charcoal:#231f20;
  --text:#3a3a3a;
  --white:#ffffff;
}
*{box-sizing:border-box;margin:0;padding:0}
html,body{width:1200px;height:1120px;overflow:hidden}
body{position:relative;background:var(--white);font-family:"PT Sans Narrow",sans-serif;color:var(--text)}
.backdrop{position:absolute;left:0;top:0;width:1200px;height:605px;background:linear-gradient(180deg,#efefef 0%,#e0e0e0 60%,#f2f2f2 100%)}
.call-band{position:absolute;left:590px;top:0}
.call-text{position:absolute;left:796px;top:4px;font:700 15px "Arimo",sans-serif;color:var(--white)}
.logo{position:absolute;left:105px;top:80px;display:flex;align-items:center;gap:14px}
.logo-dot{width:68px;height:68px;border-radius:50%;background:var(--red)}
.logo-name{font:400 58px "Oswald",sans-serif;color:var(--charcoal);line-height:1}
.social{position:absolute;left:880px;top:123px;display:flex;align-items:center}
.social-label{font:700 12px "Arimo",sans-serif;color:var(--charcoal);margin-right:5px}
.social-dot{width:35px;height:35px;border-radius:50%;background:#3b3b3b;margin-left:8px}
.nav{position:absolute;left:99px;top:171px;width:1003px;height:31px;background:var(--red)}
.nav-home{position:absolute;left:0;top:0}
.nav-links{position:absolute;left:0;top:0;list-style:none}
.nav-links li{position:absolute;top:3px;font:400 19px "Oswald",sans-serif;color:var(--white);white-space:nowrap;letter-spacing:-.5px}
.hero{position:absolute;left:100px;top:202px;width:1002px;height:402px;background:linear-gradient(90deg,#f4f4f4 0%,#e2e2e2 60%,#d8d8d8 100%)}
.hero-photo{position:absolute;left:0;top:0;width:560px;height:402px;background:linear-gradient(135deg,#d6c9c2 0%,#b8474f 40%,#e9d5d5 70%,#cfcfcf 100%)}
.hero-title{position:absolute;left:579px;top:66px;font:400 50px "Oswald",sans-serif;color:#111;letter-spacing:-1px;white-space:nowrap}
.field{position:absolute;background:var(--white);border:1px solid #bdbdbd;border-radius:3px;font:11px "Arimo",sans-serif;color:#444;padding:9px 7px}
.submit{position:absolute;left:866px;top:280px;width:77px;height:31px;background:var(--red-dark);border-radius:4px;color:var(--white);font:400 19px "Oswald",sans-serif;text-align:center;line-height:30px}
.red-band{position:absolute;left:0;top:604px;width:1200px;height:12px;background:var(--red)}
.welcome{position:absolute;left:99px;top:615px;height:86px;padding:6px 16px 0 16px;background:var(--red);clip-path:polygon(0 0,100% 0,100% 70%,50% 100%,0 70%);font:300 38px "Oswald",sans-serif;color:var(--white);letter-spacing:-.5px;white-space:nowrap;line-height:48px}
.about{position:absolute;left:99px;top:744px;width:521px}
.about h2{font:400 30px "Oswald",sans-serif;color:#111;letter-spacing:-.8px;margin-bottom:2px}
.about p{font-size:16px;line-height:19.2px;text-align:justify;margin-bottom:19px;letter-spacing:-.1px}
.divider{position:absolute;top:742px;width:1px;height:306px;background:#d8d8d8}
.card{position:absolute;top:730px}
.card h3{font:400 29px "Oswald",sans-serif;color:var(--red);letter-spacing:-1px;white-space:nowrap}
.card-photo{position:absolute;background:linear-gradient(135deg,#ececec,#9a9a9a)}
.card p{position:absolute;font-size:16px;line-height:20px;text-align:justify;letter-spacing:-.1px}
.learn{position:absolute;font:13px "Arimo",sans-serif;color:var(--red);white-space:nowrap}
.copyright{position:absolute;left:880px;top:1069px;width:203px;height:40px;background:#f5f5f5;border:1px solid #dcdcdc;border-bottom:0;font:11px "Arimo",sans-serif;color:#222;text-align:center;line-height:40px}
.footer-band{position:absolute;left:0;top:1108px;width:1200px;height:12px;background:var(--red)}
</style>
</head>
<body>
<div class="backdrop" role="img" aria-label="Faded photo of a cafe street front with palm trees"></div>

<svg class="call-band" width="560" height="40" viewBox="0 0 560 40" aria-hidden="true">
  <path d="M0 0 H555 Q545 30 490 36 H60 Q20 30 0 0Z" fill="#c9c9c9"/>
  <path d="M10 0 H540 Q530 24 480 28 H70 Q30 24 10 0Z" fill="var(--red)"/>
</svg>
<div class="call-text">Call us at&nbsp; 0-000-000-0000</div>

<header class="logo">
  <span class="logo-dot"></span>
  <span class="logo-name">Falcon IT</span>
</header>

<div class="social">
  <span class="social-label">Follow Us On</span>
  <span class="social-dot"></span>
  <span class="social-dot"></span>
  <span class="social-dot"></span>
</div>

<nav class="nav">
  <svg class="nav-home" width="52" height="31" viewBox="0 0 52 31" aria-label="Home">
    <path d="M0 0 H36 L51 15.5 L36 31 H0Z" fill="#111"/>
    <path d="M18 10 L11 16 H13 V22 H17 V18 H19 V22 H23 V16 H25Z" fill="#fff"/>
  </svg>
  <ul class="nav-links">
    <li style="left:487px">HOME</li>
    <li style="left:587px">WHAT WE ARE</li>
    <li style="left:732px">WHAT WE OFFER</li>
    <li style="left:888px">CONTACT US</li>
  </ul>
</nav>

<section class="hero">
  <div class="hero-photo" role="img" aria-label="Photo of two business people smiling at a desk with a laptop and coffee cup"></div>
  <h1 class="hero-title">Let’s Meet For Coffee’</h1>
  <div class="field" style="left:582px;top:154px;width:181px;height:30px">Name</div>
  <div class="field" style="left:770px;top:154px;width:181px;height:30px">Contact No.</div>
  <div class="field" style="left:584px;top:195px;width:180px;height:30px">Email</div>
  <div class="field" style="left:584px;top:235px;width:181px;height:30px">Address</div>
  <div class="field" style="left:771px;top:195px;width:181px;height:70px">Message</div>
  <div class="submit">Submit</div>
</section>

<div class="red-band"></div>
<h2 class="welcome">Welcome To Falcon IT</h2>

<section class="about">
  <h2>LITTLE ABOUT FALCON</h2>
  <p>We offer specialised point of sale (POS) support to the hospitality industry. We already support hundreds of cafes and restaurants. We are also about to launch and promote a range of new services with the offering of General IT Support being the most important. Other additional services to be offered are Falcon Vault Storage, reselling and supporting Corvel Shieldware.</p>
  <p>We offer specialised point of sale (POS) support to the hospitality industry. We already support hundreds of cafes and restaurants. We are also about to launch and promote a range of new services with the offering of General IT Support being the most important. Other additional services to be offered are Falcon Vault Storage, reselling and supporting Corvel Shieldware.</p>
</section>

<div class="divider" style="left:639px"></div>
<div class="divider" style="left:872px"></div>

<section class="card" style="left:660px">
  <h3>WHAT WE OFFER</h3>
  <div class="card-photo" style="left:1px;top:49px;width:187px;height:99px" role="img" aria-label="Photo of a businessman looking at website screens"></div>
  <p style="left:-2px;top:154px;width:197px">Lorem ipsum dolor sit amet, consectetuer adipiscing elit, sed diam nonummy nibh euismod tincidunt ut laoreet dolore magna aliquam erat volutpat. Ut wisi enim ...</p>
  <span class="learn" style="left:118px;top:280px">» Learn More</span>
</section>

<section class="card" style="left:896px">
  <h3>WHY CHOOSE US</h3>
  <div class="card-photo" style="left:-8px;top:46px;width:198px;height:126px" role="img" aria-label="Photo of a smiling businesswoman with colleagues in a meeting"></div>
  <p style="left:-9px;top:174px;width:197px">sectetuer adipiscing elit, sed diam nonummy nibh euismod tincidunt ut laoreet dolore magna aliquam erat volutpat. Ut wisi enim ...</p>
  <span class="learn" style="left:112px;top:280px">» Learn More</span>
</section>

<footer>
  <div class="copyright">Copyright 2012. All rights reserved.</div>
  <div class="footer-band"></div>
</footer>
</body>
</html>
```